Social Media Graphics - ALL TEXT KB

We are looking for a series of social media graphics for Instagram (standard size 1:1 (1080x1080px) that are ALL TEXT. We want the following quotes below on each graphic; one quote per graphic. AND, In very small letters at the bottom of each graphic, add @KBWardleOnline

The look and feel of these graphics should be complimentary to the color palette attached below; but keep them simple. But the design is up to you; at the end of this document, I provided various samples of all text graphics that I like as examples.

Target Market(s)

women looking to lose weight

Industry/Entity Type

health and wellness

Colors
E54698
E96AAD
F1A4CE
F9D9EA
FCEFF6

Requirements
Must have
• the quotes in the document
Should not have
• no stock photography

```html
<!DOCTYPE html>
<html lang="en">
<head>
<meta charset="utf-8">
<title>KB Quote Graphic</title>
<link rel="stylesheet" href="https://fonts.googleapis.com/css2?family=Jost:ital,wght@0,600;1,600&display=swap">
<style>
  :root {
    --pink-bright: #e8067f;
    --pink-warm: #ef3a98;
    --pink-soft: #e96aad;
    --blush: #ffcfe7;
    --shadow-plum: #8e1a5c;
  }
  html, body {
    margin: 0;
    padding: 0;
    width: 1200px;
    height: 1200px;
    overflow: hidden;
  }
  .quote-card {
    position: relative;
    width: 1200px;
    height: 1200px;
    overflow: hidden;
    background: linear-gradient(135deg, var(--pink-warm) 0%, var(--pink-bright) 55%, var(--pink-bright) 100%);
    font-family: "Jost", "Futura", sans-serif;
  }
  .texture-field {
    position: absolute;
    inset: 0;
    background:
      radial-gradient(ellipse at 15% 5%, rgba(233,106,173,0.55), transparent 45%),
      radial-gradient(ellipse at 10% 75%, rgba(200,30,120,0.35), transparent 40%);
  }
  .frame-art {
    position: absolute;
    inset: 0;
    width: 1200px;
    height: 1200px;
  }
  .frame-line {
    fill: none;
    stroke-width: 28;
    stroke-linejoin: round;
  }
  .frame-line--shadow { stroke: var(--shadow-plum); opacity: 0.55; }
  .frame-line--main { stroke: var(--blush); }
  .quote-mark--shadow { fill: var(--shadow-plum); opacity: 0.55; }
  .quote-mark--main { fill: var(--blush); }
  .quote-text {
    position: absolute;
    left: 190px;
    top: 398px;
    width: 920px;
    margin: 0;
    text-align: center;
    font-style: italic;
    font-weight: 600;
    font-size: 74px;
    line-height: 106px;
    letter-spacing: 1px;
    color: var(--blush);
    text-shadow: 4px 4px 0 var(--shadow-plum);
  }
  .quote-text span { display: block; white-space: nowrap; }
  .handle {
    position: absolute;
    left: 0;
    right: 0;
    top: 1136px;
    margin: 0;
    text-align: center;
    font-weight: 600;
    font-size: 27px;
    color: var(--blush);
  }
</style>
</head>
<body>
  <main class="quote-card">
    <div class="texture-field" role="img" aria-label="Soft pink halftone dot texture across the background"></div>

    <svg class="frame-art" viewBox="0 0 1932 1932" aria-hidden="true">
      <g transform="translate(18 18)">
        <path class="frame-line frame-line--shadow" d="M497 352 H292 A60 60 0 0 0 232 412 V1505 A60 60 0 0 0 292 1565 H1250"/>
        <path class="quote-mark--shadow" d="M497 337 L533 268 H568 L548 337 H583 V435 H497 Z"/>
        <path class="quote-mark--shadow" d="M605 337 L641 268 H676 L656 337 H692 V435 H605 Z"/>
        <path class="quote-mark--shadow" d="M1250 1480 H1336 V1578 L1300 1645 H1265 L1285 1578 H1250 Z"/>
        <path class="quote-mark--shadow" d="M1359 1480 H1445 V1578 L1409 1645 H1374 L1394 1578 H1359 Z"/>
      </g>
      <path class="frame-line frame-line--main" d="M497 352 H292 A60 60 0 0 0 232 412 V1505 A60 60 0 0 0 292 1565 H1250"/>
      <path class="quote-mark--main" d="M497 337 L533 268 H568 L548 337 H583 V435 H497 Z"/>
      <path class="quote-mark--main" d="M605 337 L641 268 H676 L656 337 H692 V435 H605 Z"/>
      <path class="quote-mark--main" d="M1250 1480 H1336 V1578 L1300 1645 H1265 L1285 1578 H1250 Z"/>
      <path class="quote-mark--main" d="M1359 1480 H1445 V1578 L1409 1645 H1374 L1394 1578 H1359 Z"/>
    </svg>

    <p class="quote-text">
      <span>One supplement, one night;</span>
      <span>your belly bloat could</span>
      <span>be gone by morning.</span>
      <span>Here's how it works!</span>
    </p>

    <p class="handle">@KBWardleOnline</p>
  </main>
</body>
</html>
```